Website transfer and revamp for consultancy

We are a professional management consultancy and need our current website transferred and modernised from Wix to WordPress with the most efficient SEO updates and blog included. We are open for options of new site set up.

Website must be relatively easy for us to maintain and update ourselves.

Website must also be desktop/mobile/ipad friendly.

www.tellvane-advisory.com

Target Market(s)

General manufacturers, construction, developers, oil and gas

Industry/Entity Type

Management Consulting

Font styles to use
Serif

Colors

Designer to choose colors to be used in the design.

Requirements
Must have
• Must have same bulk content as the existing website as a minimum with the addition of a blog page. We are open to added content.
Nice to have
• Open to designer additions such as "projects completed" and "value created" number generators
Should not have
• DO NOT USE stock photos which are not free for use to use.

```html
<!DOCTYPE html>
<html lang="en">
<head>
<meta charset="utf-8">
<title>Tellvane – The Contract and Conflict Advisory</title>
<link rel="stylesheet" href="https://fonts.googleapis.com/css2?family=Crimson+Text:wght@400;600;700&family=Mulish:wght@400;600;700&display=swap">
<style>
:root{
  --navy:#1b4a6e;
  --navy-dark:#143a58;
  --red:#c8202f;
  --ink:#3a3f45;
  --muted:#6b7178;
  --light:#eef0f2;
  --line:#d6d9dd;
  --white:#ffffff;
  --footer:#2d2d2f;
}
*{box-sizing:border-box;margin:0;padding:0}
html,body{width:1200px;height:4138px;overflow:hidden}
body{font-family:"Mulish",Arial,sans-serif;color:var(--ink);background:var(--white);position:relative}
section,header,footer{position:absolute;left:0;width:1200px}
.center{text-align:center}

/* top bar */
.topbar{position:absolute;left:0;width:1200px;top:0;height:44px;border-top:5px solid var(--navy);background:var(--white)}
.topbar .mail{position:absolute;right:310px;top:12px;font-size:16px;color:var(--muted);display:flex;align-items:center;gap:10px}
.topbar .phone{position:absolute;right:80px;top:0;height:50px;width:220px;background:var(--red);color:var(--white);font-size:18px;font-weight:600;display:flex;align-items:center;justify-content:center;gap:10px;border-radius:0 0 6px 6px}

/* header */
.site-header{top:44px;height:138px}
.brand{position:absolute;left:80px;top:60px;font-family:"Crimson Text",Georgia,serif;font-size:36px;font-weight:600;color:var(--navy);letter-spacing:1px;display:flex;align-items:center;gap:12px}
.brand .mark{width:16px;height:16px;background:var(--red)}
.nav{position:absolute;right:80px;top:62px;display:flex;gap:34px;font-size:18px;color:var(--ink)}
.nav .active{color:var(--navy);font-weight:600}

/* hero */
.hero{top:182px;height:558px;background:var(--light)}
.hero h1{position:absolute;left:80px;top:186px;font-family:"Crimson Text",Georgia,serif;font-weight:400;font-size:70px;color:var(--navy);letter-spacing:1px}
.hero p{position:absolute;left:80px;top:282px;font-size:30px;color:var(--ink)}
.hero .photo{position:absolute;left:580px;top:0;width:620px;height:558px;background:linear-gradient(160deg,#e3e6ea 0%,#c9ced5 45%,#3b4452 100%)}

/* cta band */
.cta-band{top:740px;height:115px;background:var(--navy)}
.cta-band h2{position:absolute;left:80px;top:32px;font-family:"Crimson Text",Georgia,serif;font-size:34px;font-weight:600;color:var(--white)}
.cta-band .btn-outline{position:absolute;right:80px;top:32px;width:176px;height:50px;border:2px solid var(--white);color:var(--white);font-family:"Crimson Text",Georgia,serif;font-size:20px;display:flex;align-items:center;justify-content:center;letter-spacing:1px}

.title{font-family:"Crimson Text",Georgia,serif;font-weight:700;font-size:50px;color:var(--navy)}
.title span{color:var(--red)}
.btn{position:absolute;left:510px;width:180px;height:48px;border:2px solid var(--navy);color:var(--navy);background:var(--white);font-family:"Crimson Text",Georgia,serif;font-size:20px;display:flex;align-items:center;justify-content:center;letter-spacing:1px;border-radius:3px}
.lead{font-size:15px;line-height:1.65;color:var(--muted)}

/* who we are */
.who{top:855px;height:690px;background:var(--white)}
.who .title{position:absolute;top:26px;width:100%}
.who .intro{position:absolute;top:100px;left:270px;width:660px}
.principles{position:absolute;top:170px;left:0;width:1200px;height:190px}
.principle-label{position:absolute;top:362px;font-size:24px;color:var(--ink);width:200px;text-align:center}
.who .quote{position:absolute;top:456px;left:180px;width:840px}
.who .btn{top:585px}

/* what we do */
.what{top:1545px;height:675px;background:var(--light)}
.what .title{position:absolute;top:36px;width:100%}
.what .donut{position:absolute;left:475px;top:122px}
.what .item{position:absolute;font-size:15px;line-height:1.6;color:var(--ink);width:250px}
.what .body{position:absolute;top:455px;left:180px;width:840px}
.what .btn{top:573px}

/* projects */
.projects{top:2220px;height:415px;background:var(--white)}
.projects .title{position:absolute;top:36px;width:100%}
.strip{position:absolute;top:111px;left:0;width:1200px;height:221px;display:flex}
.strip .shot{flex:1;height:221px}
.shot.a{background:linear-gradient(135deg,#6c737c,#2f3640)}
.shot.b{background:linear-gradient(135deg,#c9ced6,#4a5462)}
.shot.c{position:relative;background:linear-gradient(135deg,#5b5f66,#2b2f35);border:8px solid var(--red)}
.shot.d{background:linear-gradient(135deg,#e9e6df,#6d7480)}
.shot.c .cap{position:absolute;left:0;right:0;top:70px;text-align:center;color:var(--white);font-size:26px}
.arrow{position:absolute;color:var(--white);font-size:28px}

/* blog */
.blog{top:2635px;height:565px;background:var(--light)}
.blog .title{position:absolute;top:36px;width:100%}
.post{position:absolute;top:110px;width:325px}
.post .img{height:220px;position:relative}
.post .date{position:absolute;left:22px;bottom:0;width:70px;height:80px;background:var(--navy);color:var(--white);text-align:center;padding-top:8px}
.post .date b{display:block;font-size:30px;font-weight:600;line-height:1.1}
.post .date small{font-size:15px;letter-spacing:1px}
.post h3{margin-top:42px;font-size:20px;font-weight:700;line-height:1.5;color:var(--ink)}
.post p{margin-top:10px;font-size:16px;line-height:1.6;color:var(--muted)}

/* contact */
.contact{top:3200px;height:607px;background:var(--white)}
.contact .title{position:absolute;top:26px;width:100%}
.card{position:absolute;top:102px;width:325px;height:168px;border:2px solid var(--line);display:flex;flex-direction:column;align-items:center;justify-content:center;gap:14px;font-size:16px;line-height:1.6;color:var(--muted);text-align:center}
.field{position:absolute;border-bottom:1px solid var(--line);height:40px;font-size:16px;color:var(--muted);padding:8px 0 0 20px}
.contact .btn{top:491px;width:146px;left:527px}

/* footer */
.site-footer{top:3807px;height:331px;background:var(--footer);color:#e5e5e5}
.site-footer .brand{position:static;justify-content:center;color:var(--white);font-size:46px;margin-top:70px}
.site-footer .links{position:absolute;top:196px;width:100%;text-align:center;font-size:16px}
.site-footer .nav2{position:absolute;top:228px;width:100%;display:flex;justify-content:center;gap:32px;font-size:16px}
.site-footer .bottom{position:absolute;top:265px;left:0;width:100%;border-top:1px solid #55575b}
.site-footer .copy{position:absolute;left:80px;top:30px;font-size:16px}
.social{position:absolute;right:80px;top:20px;display:flex;gap:12px}
.social span{width:40px;height:40px;border-radius:50%;border:2px solid #e5e5e5;display:block}
</style>
</head>
<body>

<div class="topbar">
  <div class="mail">
    <svg width="18" height="13" viewBox="0 0 18 13"><rect x="0.5" y="0.5" width="17" height="12" fill="none" stroke="#6b7178"/><path d="M1 1l8 6 8-6" fill="none" stroke="#6b7178"/></svg>
    info@tellvane-advisory.com
  </div>
  <div class="phone">
    <svg width="16" height="16" viewBox="0 0 24 24"><path fill="#fff" d="M6.6 10.8a15 15 0 006.6 6.6l2.2-2.2a1 1 0 011-.25 11.4 11.4 0 003.6.57 1 1 0 011 1V20a1 1 0 01-1 1A17 17 0 013 4a1 1 0 011-1h3.5a1 1 0 011 1c0 1.25.2 2.45.57 3.6a1 1 0 01-.25 1z"/></svg>
    0044 (0)28 90 555 014
  </div>
</div>

<header class="site-header">
  <div class="brand"><span class="mark"></span>TELLVANE</div>
  <nav class="nav">
    <span class="active">Home</span><span>About</span><span>Conflict Advisory</span><span>Contract Advisory</span><span>Articles</span><span>Contact</span>
  </nav>
</header>

<section class="hero">
  <h1>TELLVANE</h1>
  <p>The Contract and Conflict Advisory</p>
  <div class="photo" role="img" aria-label="Photo of two business consultants standing with arms crossed"></div>
</section>

<section class="cta-band">
  <h2>For More Info Contact us Now</h2>
  <div class="btn-outline">CONTACT US</div>
</section>

<section class="who">
  <h2 class="title center">Who <span>We Are</span></h2>
  <p class="lead center intro">We believe that with the right solutions, we can prepare our clients for a high value and conflict free future with the application of our core principles:</p>
  <svg class="principles" viewBox="0 0 1200 190">
    <line x1="300" y1="95" x2="520" y2="95" stroke="#c9cdd2" stroke-width="3"/>
    <line x1="670" y1="95" x2="890" y2="95" stroke="#c9cdd2" stroke-width="3"/>
    <circle cx="375" cy="95" r="7" fill="#c8202f"/>
    <circle cx="827" cy="95" r="7" fill="#c8202f"/>
    <g fill="none" stroke="#c9cdd2" stroke-width="3">
      <circle cx="234" cy="95" r="74"/><circle cx="593" cy="95" r="74"/><circle cx="957" cy="95" r="74"/>
    </g>
    <g fill="#fff" stroke="#e1e4e7" stroke-width="2">
      <circle cx="234" cy="95" r="60"/><circle cx="593" cy="95" r="60"/><circle cx="957" cy="95" r="60"/>
    </g>
    <g fill="#1b4a6e">
      <rect x="200" y="86" width="36" height="18" rx="9"/>
      <rect x="232" y="86" width="36" height="18" rx="9"/>
      <rect x="571" y="80" width="44" height="9"/>
      <rect x="571" y="101" width="44" height="9"/>
    </g>
    <g fill="none" stroke="#1b4a6e" stroke-width="7" stroke-linecap="round">
      <rect x="936" y="92" width="22" height="34" rx="11" transform="rotate(45 947 109)"/>
      <rect x="956" y="64" width="22" height="34" rx="11" transform="rotate(45 967 81)"/>
    </g>
  </svg>
  <div class="principle-label" style="left:134px">integrity</div>
  <div class="principle-label" style="left:493px">equality</div>
  <div class="principle-label" style="left:857px">strength</div>
  <p class="lead center quote">"If value, whether financial or relational is not achieved, then we are not finished, we have only just begun."<br>Observing the magnitude of contractual engagements and conflicts, we believe we can make things better, better engagements, better awareness, better performance, which all lead to better value in terms of financial benefit and relationship maintenance.</p>
  <div class="btn">KNOW MORE</div>
</section>

<section class="what">
  <h2 class="title center">What <span>We Do</span></h2>
  <svg class="donut" width="250" height="250" viewBox="0 0 250 250">
    <circle cx="125" cy="125" r="95" fill="none" stroke="#1b4a6e" stroke-width="38"/>
    <circle cx="125" cy="125" r="95" fill="none" stroke="#c8202f" stroke-width="38" stroke-dasharray="290 597" transform="rotate(-80 125 125)"/>
    <g font-family="Mulish, sans-serif" font-size="15" font-weight="700" fill="#3a3f45" text-anchor="middle">
      <circle cx="58" cy="58" r="19" fill="#fff" stroke="#d6d9dd"/><text x="58" y="63">04</text>
      <circle cx="192" cy="58" r="19" fill="#fff" stroke="#d6d9dd"/><text x="192" y="63">01</text>
      <circle cx="58" cy="192" r="19" fill="#fff" stroke="#d6d9dd"/><text x="58" y="197">03</text>
      <circle cx="192" cy="192" r="19" fill="#fff" stroke="#d6d9dd"/><text x="192" y="197">02</text>
    </g>
  </svg>
  <div class="item" style="left:190px;top:166px">provide, Implement and Monitor Effective performance Solutions.</div>
  <div class="item" style="left:770px;top:166px">Create Transparency and Trust Between Parties;</div>
  <div class="item" style="left:200px;top:340px;text-align:right;width:242px">Cultivate Significant<br>Client Value;</div>
  <div class="item" style="left:770px;top:340px">Strengthen Contractual Relationship;</div>
  <p class="lead center body">We believe that the each partys goal matters, which can be achieved through collaborative working, maintaining in equilibrium as a contractual partnership or alliance.<br>It is on this premise we aim to deliver and maintaining the contract integrity and high performance contracts from inception through the contract life.</p>
  <div class="btn">KNOW MORE</div>
</section>

<section class="projects">
  <h2 class="title center">Projects <span>Completed</span></h2>
  <div class="strip">
    <div class="shot a" role="img" aria-label="Photo of a team meeting around a table"></div>
    <div class="shot b" role="img" aria-label="Photo of colleagues in a business discussion"></div>
    <div class="shot c" role="img" aria-label="Photo of documents and a pen on a desk">
      <div class="cap">Project Name</div>
      <svg style="position:absolute;left:128px;top:118px" width="30" height="30" viewBox="0 0 30 30"><g fill="none" stroke="#fff" stroke-width="3"><rect x="3" y="13" width="10" height="16" rx="5" transform="rotate(45 8 21)"/><rect x="15" y="1" width="10" height="16" rx="5" transform="rotate(45 20 9)"/></g></svg>
    </div>
    <div class="shot d" role="img" aria-label="Photo of a laptop with a chart and a handshake"></div>
  </div>
  <span class="arrow" style="left:14px;top:200px">&#8249;</span>
  <span class="arrow" style="right:14px;top:200px">&#8250;</span>
</section>

<section class="blog">
  <h2 class="title center">Latest <span>Blog</span></h2>
  <article class="post" style="left:77px">
    <div class="img" role="img" aria-label="Photo of business people talking at a desk" style="background:linear-gradient(135deg,#d9dde2,#5a6573)"><div class="date"><b>17</b><small>MAY</small></div></div>
    <h3>Lorem Ipsum is simply dummy text of the printing.</h3>
    <p>Lorem Ipsum is simply dummy text of the printing and typesetting industry. Lorem Ipsum has been the industry's standard.</p>
  </article>
  <article class="post" style="left:437px">
    <div class="img" role="img" aria-label="Photo of two professionals reviewing a tablet" style="background:linear-gradient(135deg,#c6ccd3,#39424f)"><div class="date"><b>17</b><small>MAY</small></div></div>
    <h3>Lorem Ipsum is simply dummy text of the printing.</h3>
    <p>Lorem Ipsum is simply dummy text of the printing and typesetting industry. Lorem Ipsum has been the industry's standard.</p>
  </article>
  <article class="post" style="left:798px">
    <div class="img" role="img" aria-label="Photo of a small group meeting in an office" style="background:linear-gradient(135deg,#e4e2dc,#4b5563)"><div class="date"><b>17</b><small>MAY</small></div></div>
    <h3>Lorem Ipsum is simply dummy text of the printing.</h3>
    <p>Lorem Ipsum is simply dummy text of the printing and typesetting industry. Lorem Ipsum has been the industry's standard.</p>
  </article>
</section>

<section class="contact">
  <h2 class="title center">Get In <span>Touch</span></h2>
  <div class="card" style="left:77px">
    <svg width="26" height="26" viewBox="0 0 24 24"><path fill="#1b4a6e" d="M6.6 10.8a15 15 0 006.6 6.6l2.2-2.2a1 1 0 011-.25 11.4 11.4 0 003.6.57 1 1 0 011 1V20a1 1 0 01-1 1A17 17 0 013 4a1 1 0 011-1h3.5a1 1 0 011 1c0 1.25.2 2.45.57 3.6a1 1 0 01-.25 1z"/></svg>
    <span>0044 (0)28 90 555 014</span>
  </div>
  <div class="card" style="left:437px">
    <svg width="22" height="30" viewBox="0 0 22 30"><path fill="#1b4a6e" d="M11 0a11 11 0 00-11 11c0 8 11 19 11 19s11-11 11-19A11 11 0 0011 0zm0 15a4 4 0 110-8 4 4 0 010 8z"/></svg>
    <span>2nd Floor Harrow House,<br>8-10 Mill Lane, Market<br>Quarter Belfast, BT2 4QX</span>
  </div>
  <div class="card" style="left:798px">
    <svg width="26" height="20" viewBox="0 0 26 20"><rect x="1.5" y="1.5" width="23" height="17" rx="2" fill="none" stroke="#1b4a6e" stroke-width="2.5"/><path d="M2 3l11 8 11-8" fill="none" stroke="#1b4a6e" stroke-width="2.5"/></svg>
    <span>info@tellvane-advisory.com</span>
  </div>
  <div class="field" style="left:80px;top:320px;width:320px">Your Name</div>
  <div class="field" style="left:440px;top:320px;width:320px">Your Email</div>
  <div class="field" style="left:800px;top:320px;width:320px">Your phone no.</div>
  <div class="field" style="left:80px;top:400px;width:1040px">Your Message</div>
  <div class="btn">SEND</div>
</section>

<footer class="site-footer">
  <div class="brand"><span class="mark"></span>TELLVANE</div>
  <div class="links">Arrange a consultation | Brochure | Privacy Policy</div>
  <div class="nav2"><span>Home</span><span>About</span><span>Conflict Advisory</span><span>Contract Advisory</span><span>Articles</span><span>Contact</span></div>
  <div class="bottom">
    <div class="copy">©TELLVANE- 2018. All Rights Reserved.</div>
    <div class="social"><span></span><span></span><span></span></div>
  </div>
</footer>

</body>
</html>
```